High end boutique food product label

We are looking for a label design to be used on our range of high end food products. We don't have a design or colour scheme in mind and are interested to see what ideas are submitted.
We would like it to feel sophisticated, chic, and eye-catching.
All of our products are handmade in Australia using Australian ingredients.
The graphics for the label will need to be scaleable to be fit a variety of labels from small squat jars with labels sized 3.5cm high and 7cm wide, to tall thin bottles with labels that are 14cm high and 4.5cm wide.
We would be interested in working with the winning designer to create these different sized labels.
The label submitted for this project should be 14cm high and 4.5cm wide, it should include our logo (file supplied in .jpeg and .ai), the product name 'Extra Virgin Olive Oil' and the size '250ml'.
This is just the front label on a bottle, we are not expecting a rear label to be created currently.
You are welcome to use any fonts you think will look good but the fonts used in our logo are Allaina Medium and Bebas Kai Regular.

```html
<!DOCTYPE html>
<html lang="en">
<head>
<meta charset="utf-8">
<title>Kestrel Pantry – Extra Virgin Olive Oil Label</title>
<link href="https://fonts.googleapis.com/css2?family=Bebas+Neue&display=swap" rel="stylesheet">
<style>
  :root {
    --backdrop: #ececec;
    --tan: #bfab82;
    --strip-green: #244f38;
    --panel-olive: #667353;
    --header-green: #0f3d22;
    --ink-light: #ffffff;
    --branch-tone: #e9ecdf;
  }
  html, body {
    margin: 0;
    padding: 0;
    width: 1200px;
    height: 960px;
    overflow: hidden;
    background: var(--backdrop);
  }
  .canvas {
    position: relative;
    width: 1200px;
    height: 960px;
  }
  .label {
    position: absolute;
    left: 455px;
    top: 30px;
    width: 290px;
    height: 900px;
    background: var(--strip-green);
    font-family: "Bebas Neue", sans-serif;
    color: var(--ink-light);
  }
  .band {
    position: absolute;
    left: 0;
    width: 100%;
    background: var(--tan);
  }
  .band--top { top: 0; height: 16px; }
  .band--bottom { bottom: 0; height: 19px; }
  .center-panel {
    position: absolute;
    left: 36px;
    width: 218px;
    top: 16px;
    height: 865px;
    background: var(--panel-olive);
  }
  .header-arch {
    position: absolute;
    left: 0;
    top: 0;
    width: 218px;
    height: 233px;
  }
  .brand-name {
    position: absolute;
    left: 0;
    top: 128px;
    width: 218px;
    text-align: center;
    font-size: 40px;
    line-height: 38px;
    letter-spacing: 1px;
    margin: 0;
    font-weight: 400;
  }
  .product-qualifier {
    position: absolute;
    left: 0;
    top: 300px;
    width: 218px;
    text-align: center;
    font-size: 40px;
    line-height: 40px;
    margin: 0;
  }
  .branch-illustration {
    position: absolute;
    left: 53px;
    top: 353px;
    width: 108px;
    height: 104px;
    border-radius: 50%;
    background: radial-gradient(circle, rgba(233,236,223,0.35), rgba(233,236,223,0) 70%);
  }
  .product-name {
    position: absolute;
    left: 0;
    top: 462px;
    width: 218px;
    text-align: center;
    font-size: 62px;
    line-height: 62px;
    margin: 0;
    font-weight: 400;
  }
  .origin-badge {
    position: absolute;
    left: 57px;
    top: 658px;
    width: 100px;
    height: 100px;
  }
  .volume {
    position: absolute;
    left: 0;
    top: 815px;
    width: 218px;
    text-align: center;
    font-size: 36px;
    line-height: 36px;
  }
</style>
</head>
<body>
<div class="canvas">
  <div class="label">
    <div class="band band--top"></div>

    <div class="center-panel">
      <svg class="header-arch" viewBox="0 0 218 233" aria-hidden="true">
        <path d="M0 110 Q0 92 18 90 Q55 32 109 32 Q163 32 200 90 Q218 92 218 110 L218 233 L0 233 Z" fill="var(--header-green)"/>
      </svg>
      <h1 class="brand-name">Kestrel<br>Pantry</h1>

      <p class="product-qualifier">Extra Virgin</p>
      <div class="branch-illustration" role="img" aria-label="Olive branch with leaves and olives"></div>
      <h2 class="product-name">Olive Oil</h2>

      <svg class="origin-badge" viewBox="0 0 100 100" aria-hidden="true">
        <circle cx="50" cy="50" r="47" fill="none" stroke="var(--ink-light)" stroke-width="2.5"/>
        <circle cx="50" cy="50" r="36" fill="none" stroke="var(--ink-light)" stroke-width="1.5"/>
      </svg>

      <div class="volume">250ML</div>
    </div>

    <div class="band band--bottom"></div>
  </div>
</div>
</body>
</html>
```